Horse related business entrepreneur needs a business card

I need a business card design for my horse related business. The enterprise is Copper Vale LLC and I have 3 businesses (headquartered at 2 locations): 1. property management where we rent horse stalls and apartments at a thoroughbred training center outside Ocala; 2. a medium sized transportation service in central Florida that sells horse bedding and removes used horse bedding from horse farms; and horse racing

```html
<!DOCTYPE html>
<html lang="en">
<head>
<meta charset="utf-8">
<title>Copper Vale Farm – Business Card</title>
<link href="https://fonts.googleapis.com/css2?family=Roboto:wght@400;500&display=swap" rel="stylesheet">
<style>
  :root {
    --stage: #2b2d31;
    --paper: #eeeeee;
    --teal: #124a64;
    --teal-back: #2c5a72;
    --teal-light: #a9c3cf;
    --copper: #d3602f;
    --ink: #3c3c3c;
    --rule: #8a8a8a;
    --white: #ffffff;
  }
  * { box-sizing: border-box; margin: 0; padding: 0; }
  html, body { width: 1200px; height: 1200px; overflow: hidden; }
  body {
    background: var(--stage);
    font-family: "Roboto", Arial, sans-serif;
    position: relative;
  }
  .card {
    position: absolute;
    left: 246px;
    width: 709px;
    height: 405px;
    overflow: hidden;
  }
  /* Front */
  .card--front { top: 166px; background: var(--paper); }
  .card--front .base-band {
    position: absolute; left: 0; right: 0; bottom: 0; height: 17px;
    background: var(--teal);
  }
  .brand-name {
    position: absolute;
    font-weight: 500;
    text-transform: uppercase;
    white-space: nowrap;
    transform: translateX(-50%);
  }
  .card--front .brand-name {
    left: 186px; top: 214px;
    font-size: 27px; letter-spacing: 2px;
    color: var(--teal);
  }
  .divider {
    position: absolute; left: 354px; top: 120px;
    width: 1.5px; height: 164px; background: var(--rule);
  }
  .contact-block { position: absolute; left: 412px; top: 128px; }
  .person-name { font-size: 21px; font-weight: 500; color: var(--copper); line-height: 1.2; }
  .person-role { font-size: 16px; color: var(--ink); line-height: 1.2; }
  .contact-list { list-style: none; margin-top: 28px; }
  .contact-list li {
    display: flex; align-items: center; gap: 11px;
    font-size: 16px; color: var(--ink); height: 20.5px;
  }
  .contact-list svg { width: 12px; height: 12px; flex: none; }
  /* Back */
  .card--back { top: 628px; background: var(--teal-back); }
  .back-photo {
    position: absolute; inset: 0;
    background: linear-gradient(180deg, #2d5a71 0%, #2a566d 45%, #33627a 70%, #2c5a72 100%);
  }
  .card--back .brand-name {
    left: 354px; top: 228px;
    font-size: 36px; letter-spacing: 3px;
    color: var(--teal-light);
  }
  .addresses {
    position: absolute; left: 0; right: 0; top: 334px;
    text-align: center; color: var(--white);
    font-size: 17px; line-height: 22px;
  }
</style>
</head>
<body>
  <section class="card card--front">
    <div class="brand-name">Copper Vale Farm</div>
    <div class="divider"></div>
    <div class="contact-block">
      <p class="person-name">Dana Whitcombe</p>
      <p class="person-role">Owner</p>
      <ul class="contact-list">
        <li>
          <svg viewBox="0 0 12 12" aria-hidden="true"><path d="M2.5 1 L4.5 1 L5 3.5 L3.8 4.5 Q5 7 7.5 8.2 L8.5 7 L11 7.5 L11 9.5 Q10.5 11 9 11 Q1 10 1 3 Q1 1.5 2.5 1 Z" fill="none" stroke="var(--copper)" stroke-width="1.2"/></svg>
          (352) 555-0147
        </li>
        <li>
          <svg viewBox="0 0 12 12" aria-hidden="true"><rect x="3" y="0.5" width="6" height="3" fill="var(--copper)"/><rect x="0.5" y="4" width="11" height="5" rx="1" fill="var(--copper)"/><rect x="3" y="8" width="6" height="3.5" fill="var(--copper)" stroke="var(--paper)" stroke-width="0.8"/></svg>
          (352) 555-0192
        </li>
        <li>
          <svg viewBox="0 0 12 12" aria-hidden="true"><rect x="0.8" y="2.5" width="10.4" height="7" fill="none" stroke="var(--copper)" stroke-width="1.1"/><path d="M0.8 2.5 L6 6.5 L11.2 2.5" fill="none" stroke="var(--copper)" stroke-width="1.1"/></svg>
          dana@coppervalefarm.com
        </li>
        <li>
          <svg viewBox="0 0 12 12" aria-hidden="true"><circle cx="6" cy="6" r="5.2" fill="none" stroke="var(--copper)" stroke-width="1.1"/><ellipse cx="6" cy="6" rx="2.2" ry="5.2" fill="none" stroke="var(--copper)" stroke-width="1"/><path d="M0.8 6 H11.2 M1.8 3.3 H10.2 M1.8 8.7 H10.2" stroke="var(--copper)" stroke-width="0.9"/></svg>
          www.coppervalefarm.com
        </li>
      </ul>
    </div>
    <div class="base-band"></div>
  </section>

  <section class="card card--back">
    <div class="back-photo" role="img" aria-label="Teal-tinted photo of riders on racehorses at a training track, trees in the background"></div>
    <div class="brand-name">Copper Vale Farm</div>
    <p class="addresses">
      118 Maple Hollow Road, Greenfield, VA 22940<br>
      2705 SW Pasture Lane, Ocala, FL 34481
    </p>
  </section>
</body>
</html>
```